Brackenridge Strength Studio Chronic Pain Flyer

Double sided DL flyer required to promote a strength training studio to sufferers of chronic pain. Flyer will be displayed in osteopathy, chiropractic and massage clinics. Flyer should be clean, professional and appeal to an older (40+) demographic.

Target Market(s)

Chronic pain sufferers. Age 40+

Industry/Entity Type

Health And Wellness

Colors

Designer to choose colors to be used in the design.

Requirements
Must have
• See attached files for text copy and logo. Image(s) of people strength training with a coach or personal trainer, as well as images depicting pain in common parts of the body (such as those pictured in the supplied mock up)
• website address: brackenridgestrengthstudio.example.com.au
• phone number : 0452 918 304
• Street address: 4/63 Juniper Hollow Rd, Brackenridge
Nice to have
• Images such as in the attached files.

```html
<!DOCTYPE html>
<html lang="en">
<head>
<meta charset="utf-8">
<title>Brackenridge Strength Studio – Chronic Pain Flyer</title>
<link rel="stylesheet" href="https://fonts.googleapis.com/css2?family=Arimo:wght@400;700&family=Roboto+Condensed:wght@700&family=Cabin:wght@400&display=swap">
<style>
  :root {
    --green: #0b9444;
    --green-mid: #5fb546;
    --green-light: #8dc63f;
    --green-pale: #d6ecb0;
    --slate: #4a5560;
    --grey-photo-a: #e4e4e4;
    --grey-photo-b: #9a9a9a;
    --ink: #111111;
    --logo-grey: #5a5a5a;
    --paper: #ffffff;
  }
  * { box-sizing: border-box; margin: 0; padding: 0; }
  html, body { width: 1170px; height: 1200px; overflow: hidden; background: var(--paper); }
  body { position: relative; font-family: "Arimo", Arial, sans-serif; color: var(--ink); }

  .panel { position: absolute; top: 12px; width: 569px; height: 1140px; overflow: hidden; border: 1px solid #777; background: var(--paper); }
  .panel--front { left: 2px; }
  .panel--back { left: 590px; }
  .panel__art { position: absolute; inset: 0; width: 100%; height: 100%; }

  .studio-name { position: absolute; text-align: center; font-family: "Arimo", Arial, sans-serif; font-weight: 700; color: var(--logo-grey); line-height: 1.05; letter-spacing: 1px; text-transform: uppercase; }
  .panel--front .studio-name { left: 40px; width: 420px; top: 98px; font-size: 38px; }
  .panel--back .studio-name { left: 134px; width: 400px; top: 62px; font-size: 36px; }

  .headline { position: absolute; color: var(--green); }
  .headline__lead { display: block; font-family: "Roboto Condensed", "Arial Narrow", sans-serif; font-weight: 700; letter-spacing: -1px; line-height: 1; }
  .headline__main { display: block; font-family: "Arimo", Arial, sans-serif; font-weight: 700; line-height: 1; letter-spacing: -1px; }

  .panel--front .headline { right: 16px; top: 522px; text-align: right; }
  .panel--front .headline__lead { font-size: 60px; line-height: 56px; }
  .panel--front .headline__main { font-size: 76px; margin-top: 4px; -webkit-text-stroke: 2px var(--paper); }

  .panel--back .headline { left: 48px; top: 198px; }
  .panel--back .headline__lead { font-size: 50px; }
  .panel--back .headline__main { font-size: 74px; margin-top: 2px; }

  .tagline { position: absolute; left: 70px; top: 324px; font-family: "Cabin", Arial, sans-serif; font-size: 22px; color: var(--green); letter-spacing: 0.5px; }

  .photo-frame { position: absolute; left: 244px; top: 372px; width: 296px; height: 254px; border: 7px solid var(--green-light); border-radius: 16px; background: linear-gradient(135deg, var(--grey-photo-b), var(--grey-photo-a) 55%, var(--grey-photo-b)); }

  .body-copy { position: absolute; left: 26px; width: 516px; font-size: 21.5px; line-height: 29.5px; text-align: justify; }
  .body-copy p + p { margin-top: 9px; }
  .panel--back .body-copy { top: 664px; }

  .contact { position: absolute; background: var(--paper); border: 5px solid var(--green-mid); border-radius: 20px; text-align: center; font-weight: 700; }
  .panel--front .contact { left: 258px; top: 1026px; width: 288px; height: 88px; padding-top: 6px; }
  .panel--front .contact__phone { font-size: 24px; line-height: 30px; }
  .panel--front .contact__line { font-size: 11.5px; line-height: 21px; }
  .panel--back .contact { left: 26px; top: 970px; width: 524px; height: 140px; padding-top: 16px; }
  .panel--back .contact__phone { font-size: 29px; line-height: 36px; }
  .panel--back .contact__line { font-size: 20px; line-height: 34px; }

  .side-label { position: absolute; top: 1160px; font-size: 29px; font-family: "Arimo", Arial, sans-serif; width: 200px; text-align: center; }
  .side-label--front { left: 180px; }
  .side-label--back { left: 796px; }
</style>
</head>
<body>

<section class="panel panel--front">
  <svg class="panel__art" viewBox="0 0 711 1425" preserveAspectRatio="none">
    <defs>
      <linearGradient id="front-green" x1="0" y1="0" x2="1" y2="1">
        <stop offset="0" stop-color="#4aa542"/>
        <stop offset="0.5" stop-color="#7dbe3e"/>
        <stop offset="1" stop-color="#a6d04e"/>
      </linearGradient>
      <linearGradient id="front-photo" x1="0" y1="0" x2="1" y2="1">
        <stop offset="0" stop-color="#d8d8d8"/>
        <stop offset="0.6" stop-color="#b0b0b0"/>
        <stop offset="1" stop-color="#e6e6e6"/>
      </linearGradient>
      <clipPath id="front-top-shape"><path d="M75 25 C380 -5 615 50 605 250 C595 450 430 690 175 695 C55 697 25 560 25 380 L25 110 C25 55 40 30 75 25 Z"/></clipPath>
      <clipPath id="front-bottom-shape"><path d="M711 520 C640 720 460 840 260 890 C120 930 70 1080 95 1425 L711 1425 Z"/></clipPath>
    </defs>
    <rect width="711" height="1425" fill="url(#front-green)"/>
    <path d="M711 420 C650 650 470 800 250 860 C110 900 50 1050 70 1425 L95 1425 C70 1080 120 930 260 890 C460 840 640 720 711 520 Z" fill="#c8e39a" opacity="0.7"/>
    <path d="M75 25 C380 -5 615 50 605 250 C595 450 430 690 175 695 C55 697 25 560 25 380 L25 110 C25 55 40 30 75 25 Z" fill="#ffffff"/>
    <path d="M711 520 C640 720 460 840 260 890 C120 930 70 1080 95 1425 L711 1425 Z" fill="#ffffff"/>
    <g role="img" aria-label="Photo: man holding his lower back, pain area glowing red" clip-path="url(#front-top-shape)">
      <rect x="28" y="305" width="530" height="395" fill="url(#front-photo)"/>
    </g>
    <g role="img" aria-label="Photo: man holding his sore shoulder and neck" clip-path="url(#front-bottom-shape)">
      <rect x="98" y="892" width="613" height="533" fill="url(#front-photo)"/>
    </g>
  </svg>

  <div class="studio-name">Brackenridge<br>Strength Studio</div>

  <h1 class="headline">
    <span class="headline__lead">HEALTH<br>THROUGH</span>
    <span class="headline__main">STRENGTH</span>
  </h1>

  <div class="contact">
    <div class="contact__phone">0452 918 304</div>
    <div class="contact__line">brackenridgestrengthstudio.example.com.au</div>
    <div class="contact__line">4/63 Juniper Hollow Rd, Brackenridge</div>
  </div>
</section>

<section class="panel panel--back">
  <svg class="panel__art" viewBox="0 0 712 1425" preserveAspectRatio="none" aria-hidden="true">
    <defs>
      <linearGradient id="back-green" x1="0" y1="0" x2="1" y2="0">
        <stop offset="0" stop-color="#3f9e48"/>
        <stop offset="1" stop-color="#8dc63f"/>
      </linearGradient>
      <linearGradient id="back-slate" x1="0" y1="0" x2="1" y2="0">
        <stop offset="0" stop-color="#2f3b45"/>
        <stop offset="1" stop-color="#6a7680"/>
      </linearGradient>
      <linearGradient id="back-pale" x1="0" y1="0" x2="1" y2="1">
        <stop offset="0" stop-color="#e9f5d4"/>
        <stop offset="1" stop-color="#8dc63f"/>
      </linearGradient>
    </defs>
    <path d="M0 0 L60 0 C20 120 20 300 60 400 C140 560 400 600 712 470 L712 560 C480 690 200 720 0 720 Z" fill="url(#back-green)"/>
    <path d="M40 330 C50 440 130 540 260 580 C400 610 560 570 712 510 L712 535 C540 605 380 630 240 602 C110 565 40 450 40 330 Z" fill="url(#back-slate)"/>
    <path d="M0 738 C250 720 500 690 712 630 L712 648 C500 705 250 738 0 754 Z" fill="#6fb043"/>
    <path d="M0 760 C260 744 500 716 712 665 L712 676 C500 728 260 756 0 770 Z" fill="#cfe6b0"/>
    <path d="M712 0 L712 140 C660 300 580 420 450 470 C600 380 680 230 712 0 Z" fill="url(#back-pale)"/>
    <path d="M712 940 C705 1200 650 1350 560 1425 L712 1425 Z" fill="url(#back-pale)"/>
  </svg>

  <div class="studio-name">Brackenridge<br>Strength Studio</div>

  <h2 class="headline">
    <span class="headline__lead">HEALTH THROUGH</span>
    <span class="headline__main">STRENGTH</span>
  </h2>
  <p class="tagline">You don’t have to live in pain.</p>

  <div class="photo-frame" role="img" aria-label="Photo: hands holding a painful knee, glowing red"></div>

  <div class="body-copy">
    <p>Strength training has been shown to improve many chronic pain conditions and is now being routinely recommended by medical and health professionals.</p>
    <p>Our private studio provides high quality strength training by expert strength coaches. we’ve helped countless people improve or eliminate chronic pain, contact us today and find out how we can help you.</p>
  </div>

  <div class="contact">
    <div class="contact__phone">0452 918 304</div>
    <div class="contact__line">brackenridgestrengthstudio.example.com.au</div>
    <div class="contact__line">4/63 Juniper Hollow Rd, Brackenridge</div>
  </div>
</section>

<div class="side-label side-label--front">FRONT</div>
<div class="side-label side-label--back">BACK</div>

</body>
</html>
```